International Petrochemical business needs a web design for Tessaro Desk system

We need a web design for a "Tessaro Desk" system for an international petrochemical company. The web site is used internally within the company. It is hosted by an internal department which provides government permit request service for other departments.

We would like to see designs of two pages using color light blue. (home page, internal page as attached).
Home Page:
1. Header has a background image and small animation. Header on home page can be taller than the header of the internal page.
2. Layout as attached.

Internal Page:
1. Header can use the same background image as the home page and can be shorter to utilize the page for content.
2. The blue icon behind every captions represent an icon. When user move mouse over this icon, it displays the caption in Thai language as a tooltip. This icon needs to be redesign.

The final design should communicate the followings:
- Excellent service provided system in terms of time and accurary
- Rapid growth of business via building petrochemical refinery plant

For Internal Page, the blue circle behind every captions represent an icon. When mouse over this icon, a tool tip showing the caption in Thai language is shown. Please also design this icon..

There are more feedbacks from customer as followed:

1. Banner should consists of 
    1.1 "Approved" stamp on paper
    1.2 An image of Garuda. It is used on every government documents in Thailand
    1.3 Image of petrochemical plant
2. Each menu item (Home, Permit, Search, etc) should have different colors. Drop down menu will use the same color as its parent menu item.
3. Overall tone of the web page should be light blue with background of the body the web page in white
4. "New Request" button should use green color with icon on it
5. Table header of each box in the body of the page should use dark blue background with text in white

Please kindly submit your revisions.
Thank you.

Reason: We get some late feedbacks from customers which was just updated to all designers.

• 1. Design for 1024x768 screen resolution
2. Use light blue theme
3. Background of header where the company logo is must have white background

```html
<!DOCTYPE html>
<html lang="en">
<head>
<meta charset="utf-8">
<title>Tessaro Desk – Home</title>
<link href="https://fonts.googleapis.com/css2?family=PT+Sans+Narrow:wght@400;700&family=Sarabun:wght@400&family=PT+Sans:wght@400;700&display=swap" rel="stylesheet">
<style>
:root{
  --blue:#19aeea;
  --blue-dark:#0d8fcb;
  --head-dark:#0f5a94;
  --head-line:#3f7fb2;
  --heading:#1a8ac4;
  --row-alt:#e4f4fc;
  --text:#333;
  --line:#cfd6da;
  --pager:#e2e2e2;
  --pager-on:#8fd6f4;
  --green:#3ea642;
  --green-dark:#2f8a33;
  --menu-home:#19aeea;
  --menu-permits:#2a86d1;
  --menu-search:#1fb3a3;
  --menu-report:#f0962a;
  --menu-admin:#8a68c6;
  --menu-help:#e05b73;
  --white:#fff;
}
*{box-sizing:border-box;margin:0;padding:0}
html,body{width:1139px;height:1200px;overflow:hidden;background:var(--white)}
body{position:relative;font-family:"PT Sans Narrow",sans-serif;color:var(--text)}
.abs{position:absolute}

.brand{left:150px;top:11px;display:flex;align-items:center;gap:6px;font-family:"PT Sans",sans-serif;font-weight:700;font-size:13px;color:var(--blue-dark)}
.brand-dot{width:24px;height:24px;border-radius:50%;background:var(--blue)}

.nav{left:151px;top:60px;width:836px;height:29px;background:var(--blue);border-radius:6px;box-shadow:0 2px 0 #cfe9f5;display:flex;align-items:center;overflow:hidden}
.nav a{color:var(--white);text-decoration:none;font-size:14px;text-align:center;height:29px;line-height:29px}
.nav .home{background:var(--menu-home)}
.nav .permits{background:var(--menu-permits)}
.nav .search-link{background:var(--menu-search)}
.nav .report{background:var(--menu-report)}
.nav .admin{background:var(--menu-admin)}
.nav .help{background:var(--menu-help)}
.search{position:absolute;right:8px;top:5px;width:109px;height:20px;border-radius:10px;background:var(--white);font-family:"PT Sans",sans-serif;font-size:10px;color:#666;line-height:20px;padding-left:8px}
.search svg{position:absolute;right:7px;top:4px}

.banner{left:152px;top:99px;width:834px;height:261px;border-radius:8px;background:linear-gradient(180deg,#8ea9c6 0%,#c4ccd2 35%,#8d8f92 70%,#55585c 100%)}
.dots{left:512px;top:339px;display:flex;gap:5px}
.dots span{width:11px;height:11px;border-radius:50%;background:var(--white)}
.dots span.on{background:#e0201f}

.dropdown{left:224px;top:89px;width:135px;height:99px;background:var(--menu-permits);padding-top:12px}
.dropdown a{display:block;color:var(--white);font-family:"PT Sans",sans-serif;font-size:11.5px;padding:0 0 12px 16px;text-decoration:none}

.title{font-size:18px;color:var(--heading)}
.grid{display:grid}
.grid .head{background:var(--head-dark);height:31px;border-radius:6px;display:grid;grid-template-columns:inherit}
.grid .head div{color:var(--white);font-size:14px;line-height:31px;text-align:center;border-left:1px solid var(--head-line)}
.grid .head div:first-child{border-left:none}
.grid .row{height:34px;display:grid;grid-template-columns:inherit;border-radius:6px}
.grid .row div{font-size:14px;line-height:34px;text-align:center;border-left:1px solid var(--line)}
.grid .row div:first-child{border-left:none}
.grid .row div.num{text-align:right;padding-right:42px}
.row.alt{background:var(--row-alt)}
.thai{font-family:"Sarabun",sans-serif;font-size:14px}
.head,.row{grid-column:1/-1}

.pager{display:flex;gap:5px}
.pager span{width:19px;height:19px;background:var(--pager);font-size:13px;text-align:center;line-height:19px;color:#444}
.pager span.on{background:var(--pager-on);color:var(--white)}

.rule{left:152px;width:835px;height:1px;background:#cfcfcf}

.new-request{left:586px;top:830px;width:400px;height:51px;background:linear-gradient(var(--green),var(--green-dark));border-radius:4px;font-size:20px;color:var(--white);display:flex;align-items:center;justify-content:center;gap:10px}

.footer{left:0;top:1074px;width:1139px;height:126px;background:linear-gradient(180deg,#6f6f93 0%,#8c6f8e 45%,#3e2d3f 100%)}
.social{left:525px;top:1100px;display:flex;gap:6px}
.social span{width:20px;height:20px;border-radius:3px}
.footer-links{left:0;width:1139px;top:1145px;text-align:center;font-size:13px;color:var(--white)}
.footer-links a{color:var(--white);padding:0 5px;text-decoration:underline}
.copy{left:0;width:1139px;top:1167px;text-align:center;font-size:13px;color:var(--white)}
</style>
</head>
<body>

<div class="abs brand"><span class="brand-dot"></span>Halvern Petrochemical</div>

<nav class="abs nav">
  <a class="home" style="width:73px">HOME</a>
  <a class="permits" style="width:81px">PERMITS</a>
  <a class="search-link" style="width:78px">SEARCH</a>
  <a class="report" style="width:80px">REPORT</a>
  <a class="admin" style="width:80px">ADMIN</a>
  <a class="help" style="width:72px">HELP</a>
  <div class="search">Search
    <svg width="11" height="11" viewBox="0 0 11 11"><circle cx="4.5" cy="4.5" r="3.3" fill="none" stroke="#888" stroke-width="1.4"/><line x1="7" y1="7" x2="10" y2="10" stroke="#888" stroke-width="1.6"/></svg>
  </div>
</nav>

<div class="abs banner" role="img" aria-label="Photo of a petrochemical refinery plant with pipes and storage tanks"></div>
<div class="abs dots"><span></span><span class="on"></span><span></span><span></span></div>

<div class="abs dropdown">
  <a>Create New Permit</a>
  <a>Transfer Role</a>
  <a>Transfer Res. Person</a>
</div>

<div class="abs title" style="left:152px;top:376px">New Requests</div>
<div class="abs grid" style="left:152px;top:405px;width:401px;grid-template-columns:120px 157px 124px">
  <div class="head"><div>Request No.</div><div>Requested &nbsp;Date</div><div>Branch</div></div>
  <div class="row"><div>56-0003</div><div>20/4/2013</div><div>GC1</div></div>
  <div class="row alt"><div>56-0003</div><div>21/4/2013</div><div>GC2</div></div>
</div>
<div class="abs pager" style="left:463px;top:518px"><span class="on">1</span><span>2</span><span>3</span><span>4</span></div>

<div class="abs title" style="left:588px;top:376px">My Working Requests</div>
<div class="abs grid" style="left:588px;top:405px;width:400px;grid-template-columns:120px 157px 123px">
  <div class="head"><div>Request No.</div><div>Requested &nbsp;Date</div><div>Status</div></div>
  <div class="row"><div>55-0200</div><div>25/3/2013</div><div>Waiting for process</div></div>
  <div class="row alt"><div>55-0210</div><div>21/4/2013</div><div>In progress</div></div>
  <div class="row"><div>55-0200</div><div>18/1/2013</div><div>Incomplete document</div></div>
  <div class="row alt"><div>55-0210</div><div>21/4/2013</div><div>Cancel requested</div></div>
</div>
<div class="abs pager" style="left:899px;top:591px"><span class="on">1</span><span>2</span><span>3</span><span>4</span></div>

<div class="abs rule" style="top:625px"></div>

<div class="abs title" style="left:152px;top:638px">Expiring Permits</div>
<div class="abs grid" style="left:152px;top:668px;width:833px;grid-template-columns:120px 157px 136px 116px 202px 102px">
  <div class="head"><div>Permit No</div><div>Expire Date</div><div>Permit Name</div><div>Branch</div><div>Required Time (Day)</div><div>Due Date</div></div>
  <div class="row" style="height:32px"><div>AB56001</div><div>25/3/2013 P</div><div>Permit Name ###10</div><div>GC1</div><div class="num">30</div><div>-40</div></div>
  <div class="row alt" style="height:32px"><div>BI05502</div><div>24/3/2013</div><div>Permit Name ###20</div><div>GC2</div><div class="num">60</div><div>15</div></div>
</div>
<div class="abs pager" style="left:157px;top:784px"><span class="on">1</span><span>2</span><span>3</span><span>4</span></div>

<div class="abs rule" style="top:817px"></div>

<div class="abs title" style="left:152px;top:832px">My In Progress Requests</div>
<div class="abs grid" style="left:152px;top:861px;width:401px;grid-template-columns:120px 157px 124px">
  <div class="head"><div>Request No.</div><div>Requested &nbsp;Date</div><div>Status</div></div>
  <div class="row"><div>56-0003</div><div>20/4/2013</div><div class="thai">หว่างดำเนินการ</div></div>
  <div class="row alt"><div>56-0003</div><div>21/4/2013</div><div class="thai">รอดำเนินการ</div></div>
</div>
<div class="abs pager" style="left:463px;top:1029px"><span class="on">1</span><span>2</span><span>3</span><span>4</span></div>

<div class="abs new-request">
  <svg width="22" height="22" viewBox="0 0 22 22" aria-hidden="true"><circle cx="11" cy="11" r="10" fill="none" stroke="#fff" stroke-width="2"/><line x1="11" y1="6" x2="11" y2="16" stroke="#fff" stroke-width="2.4"/><line x1="6" y1="11" x2="16" y2="11" stroke="#fff" stroke-width="2.4"/></svg>
  NEW REQUEST
</div>
<div class="abs title" style="left:588px;top:892px">Recent Completed Requests</div>
<div class="abs grid" style="left:588px;top:921px;width:400px;grid-template-columns:120px 280px">
  <div class="head"><div>Request No.</div><div style="text-align:left;padding-left:37px">Completed Date</div></div>
  <div class="row"><div>56-0003</div><div style="text-align:left;padding-left:51px">20/4/2013</div></div>
  <div class="row alt"><div>56-0003</div><div style="text-align:left;padding-left:51px">21/4/2013</div></div>
</div>
<div class="abs pager" style="left:899px;top:1034px"><span class="on">1</span><span>2</span><span>3</span><span>4</span></div>

<div class="abs footer" role="img" aria-label="Night photo of an illuminated refinery plant under a dusky sky"></div>
<div class="abs social">
  <span style="background:#3b5b9a"></span>
  <span style="background:#f08a24"></span>
  <span style="background:#33b5e5"></span>
  <span style="background:#1f6fa8"></span>
</div>
<div class="abs footer-links"><a>Home</a>|<a>Permits</a>|<a>Search</a>|<a>Report</a><a>Admin</a>|<a>Help</a></div>
<div class="abs copy">Copyrights @ 2013 All Rights Reserved</div>

</body>
</html>
```